Redesign Craft Brewing Recipe Website

Originally built with Bootstrap just to get the site going, I am seeking a complete redesign of the sites home page and recipe page. I am an experienced web developer with no graphic background, initially just looking for psd mocks.

I prefer styles that are clean and modern, and would prefer anything that is fun, engaging, and has an organic feel to it. I currently have a cartoon rabbit as a logo, but it needs some modification/tweaking, so any help in that area would be great as well.

Current site:
http://kettlewren.plumhostsite.net/

Current launch page/logo:
http://www.kettlewren.com/

I like the overall layout of the elements currently, but the design sucks.

The launch page is at the following URL

Reason: Still looking for a more modern design. Designs received so far are too similar to the original.

My site is content based and does not contain images or products. Your design should not consist of large images.

Reason: The website has very little images, so the designs need to be more text and content based. The header needs to be very small and should not contain an ad rotater.

Target Market(s)

Home brewers, Craft brewers, Microbreweries, Brewpubs

Requirements
Must have
• Web 2.0 Look and Feel, Fun, Hip, Focus on content
Should not have
• A large photo as a header

```html
<!DOCTYPE html>
<html lang="en">
<head>
<meta charset="utf-8">
<title>Kettlewren – Craft Beer Recipes</title>
<link href="https://fonts.googleapis.com/css2?family=Lato:wght@400;700;900&display=swap" rel="stylesheet">
<style>
:root{
  --page:#f6f1e8;
  --header-dark:#4a240f;
  --wood:#8b5a2f;
  --wood-light:#b07a45;
  --orange:#f2870f;
  --orange-deep:#d9661a;
  --sage:#7c9f88;
  --ink:#3a3a3a;
  --muted:#6d6258;
  --link:#4f8a5a;
  --yellow:#f7c500;
  --extract:#6aa321;
  --partial:#f06a0c;
  --allgrain:#e3352a;
  --style:#8f8f8f;
  --srm-gray:#6a6a6a;
  --srm-teal:#3bb3a6;
  --srm-amber:#c98352;
  --srm-blue:#3d8fbe;
  --line:#ddd6cb;
}
*{box-sizing:border-box;margin:0;padding:0}
html,body{width:1200px;height:2268px;overflow:hidden}
body{position:relative;background:var(--page);font-family:"Lato",sans-serif;color:var(--ink)}
.abs{position:absolute}

/* header */
.header-band{left:0;top:0;width:1200px;height:115px;background:linear-gradient(#3d1c0b,var(--header-dark))}
.header-wood{left:0;top:115px;width:1200px;height:75px;background:linear-gradient(var(--wood),var(--wood-light) 55%,var(--page))}
.nav-btn{top:23px;height:37px;background:var(--yellow);border-radius:6px;border:2px solid #c89600;display:flex;align-items:center;gap:8px;padding:0 12px;font-weight:900;font-size:18px;color:#2b1a08;white-space:nowrap}
.nav-btn svg{width:18px;height:20px}
.btn-recipes{left:139px;width:116px}
.btn-login{left:943px;width:116px}
.brand-name{left:0;top:40px;width:1200px;text-align:center;font-weight:900;font-size:50px;letter-spacing:2px;color:#fff;text-transform:uppercase}
.social{top:223px;height:18px;border-radius:3px;background:#fff;border:1px solid #c9c9c9}

.tagline{left:0;top:258px;width:1200px;text-align:center;font-size:31px;color:var(--muted);letter-spacing:.5px;white-space:nowrap}
.divider{left:143px;top:314px;width:915px;border-top:2px dotted #b9ada0}

/* sidebar */
.sidebar{left:145px;top:342px;width:204px;height:494px;background:#fff;border:5px solid #efe6da;border-radius:10px;box-shadow:0 1px 4px rgba(0,0,0,.15);padding:12px 12px}
.search{display:flex;height:30px;margin-bottom:18px}
.search span{flex:1;border:1px solid #ccc;font-size:13px;padding:6px 8px}
.search b{width:30px;background:#5a2a12;color:#fff;font-size:13px;display:flex;align-items:center;justify-content:center;border-radius:0 3px 3px 0}
.side-head{font-size:16px;color:var(--orange-deep);text-transform:uppercase;border-bottom:1px solid var(--line);padding-bottom:6px;margin-bottom:8px}
.side-list{list-style:none;margin-bottom:18px}
.side-list li{font-size:12px;height:23.5px;display:flex;align-items:center;gap:10px;color:#333;white-space:nowrap}
.side-list li::before{content:"";width:11px;height:11px;border:1px solid #bbb;background:#f7f7f7}

/* tabs */
.tab{top:343px;height:35px;font-size:22px;display:flex;align-items:center;justify-content:center;clip-path:polygon(0 0,85% 0,100% 100%,0 100%)}
.tab-recent{left:372px;width:170px;background:var(--orange);color:#fff;font-weight:700}
.tab-popular{left:540px;width:172px;background:#e6e0d6;color:#9a948c}
.tab-rule{left:372px;top:377px;width:686px;height:4px;background:var(--orange)}

/* recipe grid */
.grid{left:372px;top:400px;display:grid;grid-template-columns:334px 334px;column-gap:19px;row-gap:23px}
.recipe{position:relative;height:229px}
.recipe-title{height:30px;display:inline-flex;align-items:center;padding:0 40px 0 10px;background:var(--sage);color:#fff;font-size:14px;clip-path:polygon(0 0,86% 0,100% 100%,0 100%);min-width:150px;white-space:nowrap}
.recipe-body{position:absolute;left:0;top:30px;width:334px;height:154px;background:linear-gradient(#fff 60%,#ebebeb);border-radius:0 4px 4px 4px;box-shadow:0 1px 4px rgba(0,0,0,.2)}
.recipe-photo{position:absolute;left:10px;top:14px;width:75px;height:75px;background:radial-gradient(circle at 45% 40%,#e0a040,#8a4a18 55%,#2a1608)}
.recipe-text{position:absolute;left:97px;top:10px;width:215px;font-size:13px;line-height:18px;color:#333}
.recipe-by{position:absolute;left:97px;top:86px;font-size:12.5px;color:#666;white-space:nowrap}
.recipe-by span{color:var(--link)}
.tags{position:absolute;left:97px;top:113px;display:flex;gap:6px}
.tag{height:24px;padding:0 10px;border-radius:3px;color:#fff;font-size:12px;font-weight:700;display:flex;align-items:center;box-shadow:0 1px 2px rgba(0,0,0,.25);white-space:nowrap}
.tag.extract{background:var(--extract)}
.tag.extract.soft{background:var(--sage)}
.tag.partial{background:var(--partial)}
.tag.allgrain{background:var(--allgrain)}
.tag.style{background:var(--style)}
.stats{position:absolute;left:34px;top:187px;display:flex}
.stat{width:58px;height:42px;background:#f4f4f4;border:1px solid #ddd;margin-left:-1px;display:flex;flex-direction:column;align-items:center;justify-content:center;text-align:center;font-size:12.5px;line-height:16px;color:#444}
.stat.srm{color:#fff;border-color:transparent}
.srm.gray{background:var(--srm-gray)}.srm.teal{background:var(--srm-teal)}.srm.amber{background:var(--srm-amber)}.srm.blue{background:var(--srm-blue)}

/* footer */
.footer-wood{left:0;top:2152px;width:1200px;height:24px;background:linear-gradient(var(--wood-light),var(--wood))}
.mailing{left:151px;top:2170px;width:896px;height:45px;background:#fff;box-shadow:0 1px 4px rgba(0,0,0,.2);display:flex;align-items:center;padding:0 6px;gap:12px;white-space:nowrap}
.mailing-title{background:#111;color:#fff;font-weight:900;font-size:18px;padding:5px 8px;text-transform:uppercase;letter-spacing:-.2px}
.mailing-copy{font-size:12px;color:#333}
.mailing-field{width:170px;height:24px;border:1px solid #bbb;border-radius:12px;font-size:11px;color:#777;display:flex;align-items:center;padding-left:10px}
.mailing-join{width:36px;height:24px;border-radius:12px;background:var(--orange);color:#fff;font-size:10px;font-weight:900;display:flex;align-items:center;justify-content:center;margin-left:-22px}
.connect{margin-left:auto;font-size:12px;font-style:italic;font-weight:700;color:#333}
.net{width:24px;height:24px;border-radius:3px}
.copyright{left:0;top:2230px;width:1200px;text-align:center;font-size:13px;color:#222}
</style>
</head>
<body>

<div class="abs header-band"></div>
<div class="abs header-wood"></div>

<div class="abs nav-btn btn-recipes">
  <svg viewBox="0 0 18 20"><path d="M3 3h10v15H3z" fill="none" stroke="#2b1a08" stroke-width="2"/><path d="M13 7h3v6h-3" fill="none" stroke="#2b1a08" stroke-width="2"/></svg>RECIPES
</div>
<div class="abs nav-btn btn-login">
  <svg viewBox="0 0 18 20"><rect x="2" y="9" width="14" height="10" rx="1" fill="#2b1a08"/><path d="M5 9V6a4 4 0 0 1 8 0v3" fill="none" stroke="#2b1a08" stroke-width="2"/></svg>LOGIN
</div>

<div class="abs brand-name">Kettlewren</div>

<div class="abs social" style="left:840px;width:56px"></div>
<div class="abs social" style="left:914px;width:66px"></div>
<div class="abs social" style="left:1002px;width:56px"></div>

<div class="abs tagline">Kettlewren is the easiest way to create and share craft beer recipes.</div>
<div class="abs divider"></div>

<aside class="abs sidebar">
  <div class="search"><span>Stout</span><b>Go</b></div>
  <div class="side-head">Brewing</div>
  <ul class="side-list"><li>Extract</li><li>Partial Mash</li><li>All Grain</li></ul>
  <div class="side-head">Styles</div>
  <ul class="side-list">
    <li>American Amber Ale</li><li>American Barleywine</li><li>American Brown Ale</li><li>American IPA</li>
    <li>American Pale Ale</li><li>American Stout</li><li>American Wheat</li><li>Applewine</li>
  </ul>
  <div class="side-head">Match Maker</div>
  <ul class="side-list"><li>Boil Size</li></ul>
</aside>

<div class="abs tab tab-recent">Recent</div>
<div class="abs tab tab-popular">Popular</div>
<div class="abs tab-rule"></div>

<main class="abs grid">
<article class="recipe"><div class="recipe-title">Oak Bastard Sweet Mead</div><div class="recipe-body"><div class="recipe-photo" role="img" aria-label="Photo of beer glasses"></div><p class="recipe-text">Lorem ipsum dolor sit amet, consectetur adipisicing elit, sed do eiusmod tempor incididunt ut labore et dolore magna aliqua.</p><p class="recipe-by">Created by <span>Dana Whitlow</span></p><div class="tags"><span class="tag extract">Extract</span><span class="tag style">Sweet Mead</span></div></div><div class="stats"><div class="stat"><span>2.24%</span><span>abv</span></div><div class="stat"><span>24</span><span>ibu</span></div><div class="stat"><span>1.006</span><span>fg</span></div><div class="stat"><span>1.022</span><span>og</span></div><div class="stat srm gray"><span>4</span><span>srm</span></div></div></article>

<article class="recipe"><div class="recipe-title">Venom Mild</div><div class="recipe-body"><div class="recipe-photo" role="img" aria-label="Photo of a splashing beer glass"></div><p class="recipe-text">Lorem ipsum dolor sit amet, consectetur adipisicing elit, sed do eiusmod tempor incididunt ut labore et dolore magna aliqua.</p><p class="recipe-by">Created by <span>Dana Whitlow</span></p><div class="tags"><span class="tag partial">PartialMash</span><span class="tag style">Mild</span></div></div><div class="stats"><div class="stat"><span>2.24%</span><span>abv</span></div><div class="stat"><span>24</span><span>ibu</span></div><div class="stat"><span>1.006</span><span>fg</span></div><div class="stat"><span>1.022</span><span>og</span></div><div class="stat srm amber"><span>4</span><span>srm</span></div></div></article>

<article class="recipe"><div class="recipe-title">Capitol Munich Helles</div><div class="recipe-body"><div class="recipe-photo" role="img" aria-label="Photo of beer glasses"></div><p class="recipe-text">Lorem ipsum dolor sit amet, consectetur adipisicing elit, sed do eiusmod tempor incididunt ut labore et dolore magna aliqua.</p><p class="recipe-by">Created by <span>Dana Whitlow</span></p><div class="tags"><span class="tag allgrain">AllGrain</span><span class="tag style">Munich Helles</span></div></div><div class="stats"><div class="stat"><span>2.24%</span><span>abv</span></div><div class="stat"><span>24</span><span>ibu</span></div><div class="stat"><span>1.006</span><span>fg</span></div><div class="stat"><span>1.022</span><span>og</span></div><div class="stat srm teal"><span>4</span><span>srm</span></div></div></article>

<article class="recipe"><div class="recipe-title">Venom English Cider</div><div class="recipe-body"><div class="recipe-photo" role="img" aria-label="Photo of a pint glass"></div><p class="recipe-text">Lorem ipsum dolor sit amet, consectetur adipisicing elit, sed do eiusmod tempor incididunt ut labore et dolore magna aliqua.</p><p class="recipe-by">Created by <span>Dana Whitlow</span></p><div class="tags"><span class="tag partial">PartialMash</span><span class="tag style">English Cider</span></div></div><div class="stats"><div class="stat"><span>2.24%</span><span>abv</span></div><div class="stat"><span>24</span><span>ibu</span></div><div class="stat"><span>1.006</span><span>fg</span></div><div class="stat"><span>1.022</span><span>og</span></div><div class="stat srm blue"><span>4</span><span>srm</span></div></div></article>

<article class="recipe"><div class="recipe-title">Honeysucker Traditional Perry</div><div class="recipe-body"><div class="recipe-photo" role="img" aria-label="Photo of a beer mug"></div><p class="recipe-text">Lorem ipsum dolor sit amet, consectetur adipisicing elit, sed do eiusmod tempor incididunt ut labore et dolore magna aliqua.</p><p class="recipe-by">Created by <span>Dana Whitlow</span></p><div class="tags"><span class="tag extract">Extract</span><span class="tag style">Traditional Perry</span></div></div><div class="stats"><div class="stat"><span>2.24%</span><span>abv</span></div><div class="stat"><span>24</span><span>ibu</span></div><div class="stat"><span>1.006</span><span>fg</span></div><div class="stat"><span>1.022</span><span>og</span></div><div class="stat srm amber"><span>4</span><span>srm</span></div></div></article>

<article class="recipe"><div class="recipe-title">Capitol Old Ale</div><div class="recipe-body"><div class="recipe-photo" role="img" aria-label="Photo of beer glasses"></div><p class="recipe-text">Lorem ipsum dolor sit amet, consectetur adipisicing elit, sed do eiusmod tempor incididunt ut labore et dolore magna aliqua.</p><p class="recipe-by">Created by <span>Dana Whitlow</span></p><div class="tags"><span class="tag extract">Extract</span><span class="tag style">Old Ale</span></div></div><div class="stats"><div class="stat"><span>2.24%</span><span>abv</span></div><div class="stat"><span>24</span><span>ibu</span></div><div class="stat"><span>1.006</span><span>fg</span></div><div class="stat"><span>1.022</span><span>og</span></div><div class="stat srm gray"><span>4</span><span>srm</span></div></div></article>

<article class="recipe"><div class="recipe-title">Honeysucker Belgian Tripel</div><div class="recipe-body"><div class="recipe-photo" role="img" aria-label="Photo of beer glasses"></div><p class="recipe-text">Lorem ipsum dolor sit amet, consectetur adipisicing elit, sed do eiusmod tempor incididunt ut labore et dolore magna aliqua.</p><p class="recipe-by">Created by <span>Dana Whitlow</span></p><div class="tags"><span class="tag extract">Extract</span><span class="tag style">Belgian Tripel</span></div></div><div class="stats"><div class="stat"><span>2.24%</span><span>abv</span></div><div class="stat"><span>24</span><span>ibu</span></div><div class="stat"><span>1.006</span><span>fg</span></div><div class="stat"><span>1.022</span><span>og</span></div><div class="stat srm teal"><span>4</span><span>srm</span></div></div></article>

<article class="recipe"><div class="recipe-title">Venom Mild</div><div class="recipe-body"><div class="recipe-photo" role="img" aria-label="Photo of a pint glass"></div><p class="recipe-text">Lorem ipsum dolor sit amet, consectetur adipisicing elit, sed do eiusmod tempor incididunt ut labore et dolore magna aliqua.</p><p class="recipe-by">Created by <span>Dana Whitlow</span></p><div class="tags"><span class="tag partial">PartialMash</span><span class="tag style">Mild</span></div></div><div class="stats"><div class="stat"><span>2.24%</span><span>abv</span></div><div class="stat"><span>24</span><span>ibu</span></div><div class="stat"><span>1.006</span><span>fg</span></div><div class="stat"><span>1.022</span><span>og</span></div><div class="stat srm amber"><span>4</span><span>srm</span></div></div></article>

<article class="recipe"><div class="recipe-title">Honeysucker Traditional Perry</div><div class="recipe-body"><div class="recipe-photo" role="img" aria-label="Photo of a splashing beer glass"></div><p class="recipe-text">Lorem ipsum dolor sit amet, consectetur adipisicing elit, sed do eiusmod tempor incididunt ut labore et dolore magna aliqua.</p><p class="recipe-by">Created by <span>Dana Whitlow</span></p><div class="tags"><span class="tag extract">Extract</span><span class="tag style">Traditional Perry</span></div></div><div class="stats"><div class="stat"><span>2.24%</span><span>abv</span></div><div class="stat"><span>24</span><span>ibu</span></div><div class="stat"><span>1.006</span><span>fg</span></div><div class="stat"><span>1.022</span><span>og</span></div><div class="stat srm amber"><span>4</span><span>srm</span></div></div></article>

<article class="recipe"><div class="recipe-title">Capitol Munich Helles</div><div class="recipe-body"><div class="recipe-photo" role="img" aria-label="Photo of beer glasses"></div><p class="recipe-text">Lorem ipsum dolor sit amet, consectetur adipisicing elit, sed do eiusmod tempor incididunt ut labore et dolore magna aliqua.</p><p class="recipe-by">Created by <span>Dana Whitlow</span></p><div class="tags"><span class="tag allgrain">AllGrain</span><span class="tag style">Munich Helles</span></div></div><div class="stats"><div class="stat"><span>2.24%</span><span>abv</span></div><div class="stat"><span>24</span><span>ibu</span></div><div class="stat"><span>1.006</span><span>fg</span></div><div class="stat"><span>1.022</span><span>og</span></div><div class="stat srm blue"><span>4</span><span>srm</span></div></div></article>

<article class="recipe"><div class="recipe-title">Venom English Cider</div><div class="recipe-body"><div class="recipe-photo" role="img" aria-label="Photo of a beer mug"></div><p class="recipe-text">Lorem ipsum dolor sit amet, consectetur adipisicing elit, sed do eiusmod tempor incididunt ut labore et dolore magna aliqua.</p><p class="recipe-by">Created by <span>Dana Whitlow</span></p><div class="tags"><span class="tag partial">PartialMash</span><span class="tag style">English Cider</span></div></div><div class="stats"><div class="stat"><span>2.24%</span><span>abv</span></div><div class="stat"><span>24</span><span>ibu</span></div><div class="stat"><span>1.006</span><span>fg</span></div><div class="stat"><span>1.022</span><span>og</span></div><div class="stat srm blue"><span>4</span><span>srm</span></div></div></article>

<article class="recipe"><div class="recipe-title">Capitol Old Ale</div><div class="recipe-body"><div class="recipe-photo" role="img" aria-label="Photo of beer glasses"></div><p class="recipe-text">Lorem ipsum dolor sit amet, consectetur adipisicing elit, sed do eiusmod tempor incididunt ut labore et dolore magna aliqua.</p><p class="recipe-by">Created by <span>Dana Whitlow</span></p><div class="tags"><span class="tag extract soft">Extract</span><span class="tag style">Old Ale</span></div></div><div class="stats"><div class="stat"><span>2.24%</span><span>abv</span></div><div class="stat"><span>24</span><span>ibu</span></div><div class="stat"><span>1.006</span><span>fg</span></div><div class="stat"><span>1.022</span><span>og</span></div><div class="stat srm gray"><span>4</span><span>srm</span></div></div></article>

<article class="recipe"><div class="recipe-title">Honeysucker Belgian Tripel</div><div class="recipe-body"><div class="recipe-photo" role="img" aria-label="Photo of beer glasses"></div><p class="recipe-text">Lorem ipsum dolor sit amet, consectetur adipisicing elit, sed do eiusmod tempor incididunt ut labore et dolore magna aliqua.</p><p class="recipe-by">Created by <span>Dana Whitlow</span></p><div class="tags"><span class="tag extract soft">Extract</span><span class="tag style">Belgian Tripel</span></div></div><div class="stats"><div class="stat"><span>2.24%</span><span>abv</span></div><div class="stat"><span>24</span><span>ibu</span></div><div class="stat"><span>1.006</span><span>fg</span></div><div class="stat"><span>1.022</span><span>og</span></div><div class="stat srm teal"><span>4</span><span>srm</span></div></div></article>

<article class="recipe"><div class="recipe-title">Venom Mild</div><div class="recipe-body"><div class="recipe-photo" role="img" aria-label="Photo of a beer mug"></div><p class="recipe-text">Lorem ipsum dolor sit amet, consectetur adipisicing elit, sed do eiusmod tempor incididunt ut labore et dolore magna aliqua.</p><p class="recipe-by">Created by <span>Dana Whitlow</span></p><div class="tags"><span class="tag partial">PartialMash</span><span class="tag style">Mild</span></div></div><div class="stats"><div class="stat"><span>2.24%</span><span>abv</span></div><div class="stat"><span>24</span><span>ibu</span></div><div class="stat"><span>1.006</span><span>fg</span></div><div class="stat"><span>1.022</span><span>og</span></div><div class="stat srm amber"><span>4</span><span>srm</span></div></div></article>
</main>

<div class="abs footer-wood"></div>
<footer class="abs mailing">
  <span class="mailing-title">Join our mailing list</span>
  <span class="mailing-copy">Sign up for our e-mail list to receive updates</span>
  <span class="mailing-field">Your e-mail address</span>
  <span class="mailing-join">JOIN</span>
  <span class="connect">Connect with us on</span>
  <span class="net" style="background:#4fb0e6"></span>
  <span class="net" style="background:#3b5998"></span>
  <span class="net" style="background:#1f78b4"></span>
</footer>
<div class="abs copyright">Copyright © 2013 Kettlewren. All rights reserved.</div>

</body>
</html>
```